Hip Music Management Co. BIz Card

I have a logo (attached) the back side of the card should the full logo on the entire card- that's it. The front side of the card should show the logo somewhere, keeping with the 4 different shades of blue. The front side of the card can be a white background with logo and colored typeface for all info. Pretty simple.

Target Market(s)

I manage and produce a whole bunch of major label and indie artists.

Industry/Entity Type

Management

Contact Information for Business Card

Velmarra Sound Collective (logo)
Dale Wortheny
President
www.velmarrasoundcollective.com
dale@velmarrasoundcollective.com
+1 415.287.6192
718 Copperfield Lane
Harlow Springs, NY 12893

Requirements
Must have
• Entire logo on back side. White background on front- unless you provide something more interesting.
Nice to have
• On the front of the card if you choose a white backgound, if possible take my logo without the blue background (over white) that would be cool.

```html
<!DOCTYPE html>
<html lang="en">
<head>
<meta charset="utf-8">
<title>Velmarra Sound Collective – Business Card</title>
<link rel="stylesheet" href="https://fonts.googleapis.com/css2?family=Roboto:wght@300;400&family=Roboto+Condensed:wght@700&display=swap">
<style>
  :root {
    --backdrop: #181f4a;
    --card: #ffffff;
    --teal: #12b3c6;
    --blue: #1b7bc2;
    --sky: #4aa8de;
  }
  * { margin: 0; padding: 0; box-sizing: border-box; }
  html, body { width: 1200px; height: 1000px; overflow: hidden; }
  body { background: var(--backdrop); position: relative; font-family: "Roboto", Arial, sans-serif; }

  .card {
    position: absolute;
    left: 321px;
    width: 544px;
    height: 319px;
    background: var(--card);
  }
  .card--back { top: 128px; display: flex; align-items: center; justify-content: center; }
  .card--front { top: 519px; }

  .wordmark {
    font-family: "Roboto Condensed", "Arial Narrow", sans-serif;
    font-weight: 700;
    color: var(--teal);
    white-space: nowrap;
    letter-spacing: 0.2px;
  }
  .card--back .wordmark { font-size: 31px; }
  .card--front .wordmark { position: absolute; left: 41px; top: 44px; font-size: 25px; }

  .holder { position: absolute; left: 37px; top: 146px; }
  .holder__name {
    font-family: "Roboto Condensed", "Arial Narrow", sans-serif;
    font-weight: 700;
    font-size: 26px;
    line-height: 30px;
    color: var(--teal);
  }
  .holder__title { font-size: 19px; line-height: 24px; color: var(--teal); font-weight: 400; }

  .contact { position: absolute; left: 37px; top: 210px; list-style: none; }
  .contact__item {
    display: flex; align-items: center; gap: 5px;
    height: 20.7px;
    font-size: 16px; font-weight: 300; color: var(--blue);
    white-space: nowrap;
  }
  .contact__icon { width: 15px; height: 15px; flex: none; }
</style>
</head>
<body>
  <section class="card card--back" aria-label="Card back">
    <span class="wordmark">Velmarra Sound Collective</span>
  </section>

  <section class="card card--front" aria-label="Card front">
    <span class="wordmark">Velmarra Sound Collective</span>

    <div class="holder">
      <p class="holder__name">Dale Wortheny</p>
      <p class="holder__title">President</p>
    </div>

    <ul class="contact">
      <li class="contact__item">
        <svg class="contact__icon" viewBox="0 0 16 16" aria-hidden="true">
          <circle cx="8" cy="8" r="7.5" fill="var(--blue)"/>
          <circle cx="8" cy="8" r="4.5" fill="none" stroke="#fff" stroke-width="1.2"/>
          <path d="M3.5 8h9M8 3.5c-2 2.5-2 6.5 0 9M8 3.5c2 2.5 2 6.5 0 9" fill="none" stroke="#fff" stroke-width="1"/>
        </svg>
        www.velmarrasoundcollective.com
      </li>
      <li class="contact__item">
        <svg class="contact__icon" viewBox="0 0 16 16" aria-hidden="true">
          <circle cx="8" cy="8" r="7.5" fill="var(--blue)"/>
          <rect x="3.5" y="5" width="9" height="6" fill="none" stroke="#fff" stroke-width="1.1"/>
          <path d="M3.5 5l4.5 3.5L12.5 5" fill="none" stroke="#fff" stroke-width="1.1"/>
        </svg>
        dale@velmarrasoundcollective.com
      </li>
      <li class="contact__item">
        <svg class="contact__icon" viewBox="0 0 16 16" aria-hidden="true">
          <circle cx="8" cy="8" r="7.5" fill="var(--blue)"/>
          <path d="M5.5 4c.6-.4 1.3 0 1.5.5l.5 1.3c.2.5-.2.9-.6 1.1.4 1.2 1 1.9 2 2.5.3-.4.7-.6 1.2-.4l1.2.6c.5.3.6 1 .2 1.5-.8.8-2 1-3.2.2C6.5 10 5 8.2 4.6 6.3c-.2-1 .2-1.8.9-2.3z" fill="#fff"/>
        </svg>
        +1 415.287.6192
      </li>
      <li class="contact__item">
        <svg class="contact__icon" viewBox="0 0 16 16" aria-hidden="true">
          <path d="M8 2a4 4 0 0 0-4 4c0 3 4 8 4 8s4-5 4-8a4 4 0 0 0-4-4z" fill="var(--blue)"/>
          <circle cx="8" cy="6" r="1.5" fill="#fff"/>
        </svg>
        718 Copperfield Lane Harlow Springs, NY 12893
      </li>
    </ul>
  </section>
</body>
</html>
```